Stellenausschreibungen für Dachdeckerbetrieb
Zielgruppe
Wir sind ein Dachdeckerbetrieb und suchen verstärkt nach Zuwachs.
Aufgabenstellung
Die Stellenausschreibungen soll schlicht und modern sein. Eine Seite, beidseitig bedruckt ist völlig ausreichend. Detailreiche, ansprechende Bilder zu unserem Dachdecker Gewerk sind erwünscht.

```html
<!DOCTYPE html>
<html lang="de">
<head>
<meta charset="utf-8">
<title>Stellenausschreibung Dachwerk- und Gründachbau-GmbH</title>
<link rel="stylesheet" href="https://fonts.googleapis.com/css2?family=Arimo:ital,wght@0,400;0,700;1,700&display=swap">
<style>
  :root{
    --green:#1f9a4c;
    --paper:#ffffff;
    --body-grey:#e9eaea;
    --ink:#222;
    --stage:#ececec;
    --photo-a:#8a7a66;
    --photo-b:#b9a48a;
  }
  *{box-sizing:border-box;margin:0;padding:0}
  html,body{width:1200px;height:675px;overflow:hidden}
  body{background:var(--stage);font-family:"Arimo",Arial,sans-serif;color:var(--ink);
    display:flex;justify-content:center;align-items:center;gap:60px}
  .sheet{position:relative;width:440px;height:622px;background:var(--paper);
    box-shadow:0 4px 14px rgba(0,0,0,.18);overflow:hidden}

  /* front */
  .front .side-strip{position:absolute;right:0;top:0;width:26px;bottom:96px;background:var(--green)}
  .front .header{position:absolute;left:0;top:0;right:26px;height:92px;display:flex;
    justify-content:space-between;align-items:center;padding:0 22px}
  .company-name{font-style:italic;font-weight:700;color:var(--green);font-size:19px;line-height:1.2}
  .brand-mark{display:flex;align-items:center;gap:7px;font-weight:700;font-size:22px;color:var(--green)}
  .brand-mark .square{width:16px;height:16px;background:var(--green)}
  .photo-band{position:absolute;left:0;right:26px;top:96px;height:94px;
    border-top:4px solid var(--green);border-bottom:4px solid var(--green)}
  .photo-band div{width:100%;height:100%;background:linear-gradient(100deg,var(--photo-a),var(--photo-b) 55%,#9aa0a3)}
  .front .body{position:absolute;left:0;right:26px;top:190px;bottom:96px;
    background:linear-gradient(#f4f4f4,var(--body-grey));padding:10px 22px 0}
  .services{text-align:center;font-size:12.5px;line-height:1.35;padding:0 22px 8px;
    border-bottom:4px solid var(--green);margin:0 -22px}
  .headline{font-style:italic;font-weight:700;color:var(--green);font-size:25px;margin:20px 0 8px}
  .intro{font-size:11px;line-height:1.35}
  .job-list{list-style:none;font-size:11px;line-height:1.4;margin:18px 0 18px 8px}
  .job-list li::before,.task-list li::before{content:"• ";color:var(--green);font-weight:700}
  .outro{font-size:11px;line-height:1.35}
  .web{font-weight:700;color:var(--green);font-size:13px;text-align:center;margin-top:22px}
  .footer{position:absolute;left:0;right:0;bottom:0;height:96px;background:var(--green);
    color:#fff;font-weight:700;font-size:13.5px;line-height:1.4;text-align:center;
    display:flex;flex-direction:column;justify-content:center}

  /* back */
  .back .side-strip{position:absolute;left:0;top:0;width:26px;bottom:96px;background:var(--green)}
  .back .content{position:absolute;left:26px;right:0;top:0;bottom:96px;padding:20px 22px 0 26px}
  .section-title{font-size:12.5px;margin:12px 0 4px}
  .task-list{list-style:none;font-size:9.5px;line-height:1.3;margin-left:14px}
  .apply{position:absolute;left:26px;right:0;bottom:104px;text-align:center;
    color:var(--green);font-weight:700;font-size:12.5px;line-height:1.35}
</style>
</head>
<body>

<section class="sheet front">
  <div class="side-strip"></div>
  <header class="header">
    <div class="company-name">Dachwerk- und<br>Gründachbau-GmbH</div>
    <div class="brand-mark"><span class="square"></span>Dachwerk</div>
  </header>
  <div class="photo-band"><div role="img" aria-label="Fotostreifen mit Dachdeckern bei der Arbeit auf einem Flachdach und Ziegeldach"></div></div>
  <div class="body">
    <p class="services">Flachdachabdichtung • Dachdeckerarbeiten • Dachfenster<br>Schieferarbeiten • Sprenglerarbeiten • Reparaturarbeiten<br>Wartung • Reparaturarbeiten</p>
    <h1 class="headline">Wir haben freie Stellen</h1>
    <p class="intro">Wir sind ein Familienunternehmen mit Sitz in Hofbach. In den vergangenen 29 Jahren sind wir gewachsen - und es gibt einiges zu tun! Für unsere vielfältigen Projekte suchen wir:</p>
    <ul class="job-list">
      <li>Dachdeckerhelfer (m/w)</li>
      <li>Vorarbeiter (m/w) im Bereich Kundendienst</li>
      <li>Abdichter (m/w) im Bereich Flachdach</li>
    </ul>
    <p class="outro">Unsere Vorstellungen und was sie von uns erwarten können, finden sie auf der Rückseite.</p>
    <p class="web">www.dachwerk-hofbach.de</p>
  </div>
  <footer class="footer">
    <span>Lindenstraße 12 • 55299 Hofbach</span>
    <span>Telefon: 06131 - 4470 - 0</span>
    <span>E-Mail: info@dachwerk-hofbach.de</span>
  </footer>
</section>

<section class="sheet back">
  <div class="side-strip"></div>
  <div class="content">
    <h2 class="section-title">Zu Ihren neuen Tätigkeiten gehören...</h2>
    <ul class="task-list">
      <li>Dachdeckerarbeiten am Neubau und Bestand</li>
      <li>Aufmaß vor Ort erstellen</li>
      <li>Steildach/Flachdach, Sanierung oder Neubau mit Ziegel oder Betondachsteinen</li>
      <li>Dachflächenfenster</li>
      <li>Reparatur und Wartung</li>
    </ul>
    <h2 class="section-title">Was wir von Ihnen erwarten...</h2>
    <ul class="task-list">
      <li>Selbstständiges Ausführen von Projektarbeiten aller Art</li>
      <li>Selbstständiges Ausführen von Reparatur- und Wartungsaufträgen</li>
      <li>Unterstützung bei Dachdecker- und Klempnerarbeiten</li>
      <li>Vorbereitungen von Projektarbeiten anhand von Leistungsverzeichnissen und Zeichnungen</li>
    </ul>
    <h2 class="section-title">Was Sie mitbringen...</h2>
    <ul class="task-list">
      <li>Sie haben eine erfolgreiche Ausbildung in einem handwerklichen Beruf abgeschlossen</li>
      <li>Sie haben eine erfolgreiche Ausbildung als Dachdeckergeselle abgeschlossen</li>
      <li>Sie besitzen eine gültige Fahrerlaubnis der Führerscheinklasse BE (früher 3)</li>
      <li>Sie besitzen vorzugsweise Berufserfahrung</li>
      <li>Ihr Kommunikationsverhalten - Sie treten freundlich und sicher auf</li>
    </ul>
    <h2 class="section-title">Was Sie von uns erwarten können...</h2>
    <ul class="task-list">
      <li>Leistungsorientiere, pünktliche und korrekte Bezahlung Ihrer Leistung, dazu gehören selbstverständlich auch Urlaubs- und Weihnachtsgeld</li>
      <li>Stellung von Arbeitskleidung</li>
      <li>Angenehmes Arbeitsklima in einem tollen Team</li>
      <li>Stetige Weiterbildung</li>
    </ul>
  </div>
  <p class="apply">Richten Sie Ihre Bewerbung bitte an info@dachwerk-hofbach.de<br>www.dachwerk-hofbach.de</p>
  <footer class="footer">
    <span>Lindenstraße 12 • 55299 Hofbach</span>
    <span>Telefon: 06131 - 4470 - 0</span>
    <span>E-Mail: info@dachwerk-hofbach.de</span>
  </footer>
</section>

</body>
</html>
```